Pet and Potrait photography business needs web site design

I need a web design that is for a portrait and pet photography business based in Tasmania, Australia. It is a small, simple concept, photography business that focuses on portraits and pet photography only. I need something that is clean, maybe a white background, fun, and appealing to families. The design must make my images stand out and be the focus. The final design needs to show that it is aimed a families, pet owners, and is all about the clients - albeit the two or four legged kinds.

Business name is: maple lantern photography

I need it to be able to have the following:

- Include space for logo design which is also through SketchPlaza
- Home Page which has a gallery of my images (which you can click an arrow - either forward or back - that showcases my images
- About Page
- Portfolio Page (preferably two a) for portraits, and b) for pet photography
- Pricing page
- secure log in client page
- Contact page
Updates

Reason: Waiting for logo design to be completed to fit in with overall website design.

Target Market(s)

Families
Pet owners
Single couples who have fur babies

Industry/Entity Type

Business

Font styles to use
Serif
Decorative
Script

Colors

Designer to choose colors to be used in the design.

Requirements
Must have
• the website must provide the ability for me to upload and change images regularly.
Nice to have
• Logo design is a secondary project that will need to be worked on as well. I will pay an additional amount for those that are prepared to include this in the project.
Should not have
• No graffiti style writing.
It has to be elegant, and stylish and be aimed at females.
Women are going to be the driver for having portraits done of either their babies, children, or fur babies - i.e. pets.

```html
<!DOCTYPE html>
<html lang="en">
<head>
<meta charset="utf-8">
<title>My Images – maple lantern photography</title>
<link rel="stylesheet" href="https://fonts.googleapis.com/css2?family=Gelasio:ital,wght@0,400;1,400&family=Arimo:wght@400;700&display=swap">
<style>
:root{
  --ink:#444;
  --ink-soft:#666;
  --muted:#999;
  --rule:#e2e2e2;
  --accent:#d7bfd9;
  --accent-text:#fff;
  --frame:#f3f3f3;
  --frame-edge:#dcdcdc;
  --footer-bg:#efefeb;
  --footer-cap:#dcdcdc;
  --base-bg:#3a3a3a;
  --base-text:#bbb;
  --button:#474747;
}
*{margin:0;padding:0;box-sizing:border-box}
html,body{width:1200px;height:1084px;overflow:hidden;background:#fff}
body{position:relative;font-family:"Arimo",Arial,sans-serif;color:var(--ink)}
.abs{position:absolute}

.brand{left:152px;top:31px;font-family:"Gelasio",Georgia,serif;color:var(--ink)}
.brand-name{font-size:25px;font-style:italic;line-height:28px;display:block;white-space:nowrap}
.brand-sub{font-size:14px;font-style:italic;color:var(--muted);margin-left:26px;display:block;line-height:18px}
.brand-dot{position:absolute;left:0;top:34px;width:18px;height:9px;border-radius:50%;background:#d4d4d4}

.nav{top:38px;left:0;width:1200px;height:35px}
.nav a{position:absolute;top:0;height:35px;line-height:35px;font-size:13px;letter-spacing:2.1px;color:var(--ink-soft);text-decoration:none}
.nav a.is-active{background:var(--accent);color:var(--accent-text);padding:0 11px;width:86px}

.header-bar{left:111px;top:104px;width:980px;height:6px;background:var(--accent)}
.crumbs{left:148px;top:120px;font-size:11.5px;color:var(--ink-soft)}
.crumbs em{font-family:"Gelasio",Georgia,serif;color:var(--muted);margin-right:4px;font-size:11px}
.crumbs-rule{left:111px;top:148px;width:980px;height:1px;background:var(--rule)}

.page-title{left:151px;top:178px;font-family:"Gelasio",Georgia,serif;font-size:21px;font-weight:400;color:var(--ink)}
.title-rule{left:153px;width:588px;height:1px;background:var(--rule)}

.album-label{left:151px;font-size:13px;letter-spacing:2.6px;color:var(--ink-soft)}

.thumb{width:116px;height:116px;background:var(--frame);border:1px solid var(--frame-edge)}
.thumb .photo{position:absolute;left:5px;top:5px;width:104px;height:104px}
.tone-a .photo{background:linear-gradient(160deg,#d9d2b8,#c8a98c 55%,#2d3b66)}
.tone-b .photo{background:linear-gradient(160deg,#e8d7b2,#c79c7d 55%,#7fa6c9)}
.tone-c .photo{background:linear-gradient(160deg,#6b7a48,#b5967a 55%,#e6e4d8)}
.tone-d .photo{background:linear-gradient(180deg,#d7dce0,#c9b58f 55%,#a8a26b)}
.chev{width:34px;height:154px}

.footer-cap{left:111px;top:713px;width:980px;height:6px;background:var(--footer-cap)}
.footer{left:111px;top:725px;width:980px;height:306px;background:var(--footer-bg)}
.col{top:759px;width:200px}
.col h3{font-size:11px;font-weight:700;letter-spacing:1.2px;color:var(--ink);margin-bottom:13px}
.col p{font-family:"Gelasio",Georgia,serif;font-style:italic;font-size:13px;line-height:20px;color:var(--muted)}
.col p + p{margin-top:20px}
.col .more{display:block;margin-top:4px;font-size:13px;color:var(--ink);text-decoration:none}
.col.contact{width:230px}
.col.contact p{color:var(--ink-soft);white-space:nowrap}
.btn{display:block;margin-top:17px;width:187px;height:29px;line-height:29px;text-align:center;background:var(--button);border-radius:3px;color:#fff;font-family:"Gelasio",Georgia,serif;font-style:italic;font-size:18px;text-decoration:none}

.base{left:111px;top:1031px;width:980px;height:53px;background:var(--base-bg)}
.copyright{left:150px;top:1050px;font-family:"Gelasio",Georgia,serif;font-style:italic;font-size:12px;color:var(--base-text)}
.base-brand{right:274px;top:1040px;text-align:right;font-family:"Gelasio",Georgia,serif;font-style:italic;color:var(--base-text);white-space:nowrap}
.base-brand-name{display:block;font-size:15px;line-height:18px}
.base-brand-sub{display:block;font-size:9px;line-height:12px}
.social{top:1044px;width:27px;height:27px;border-radius:50%;background:#8a8a8a}
</style>
</head>
<body>

<header>
  <div class="abs brand">
    <span class="brand-name">maple lantern</span>
    <span class="brand-dot"></span>
    <span class="brand-sub">Photography</span>
  </div>
  <nav class="abs nav">
    <a href="#" style="left:499px">HOME</a>
    <a href="#" style="left:571px">ABOUT</a>
    <a href="#" style="left:651px">PORTFOLIO</a>
    <a href="#" style="left:776px">PRICING</a>
    <a href="#" class="is-active" style="left:860px">LOGOUT</a>
    <a href="#" style="left:976px">CONTACT</a>
  </nav>
  <div class="abs header-bar"></div>
  <div class="abs crumbs"><em>You are here:</em> Home » My Images</div>
  <div class="abs crumbs-rule"></div>
</header>

<main>
  <h1 class="abs page-title">My Images</h1>
  <div class="abs title-rule" style="top:217px"></div>
  <div class="abs title-rule" style="top:250px"></div>

  <div class="abs album-label" style="top:251px">ALBUM 1</div>
  <svg class="abs chev" style="left:113px;top:276px" viewBox="0 0 34 154"><polyline points="33,1 2,77 33,153" fill="none" stroke="#ccc" stroke-width="2"/></svg>
  <svg class="abs chev" style="left:1053px;top:276px" viewBox="0 0 34 154"><polyline points="1,1 32,77 1,153" fill="none" stroke="#ccc" stroke-width="2"/></svg>
  <div class="abs thumb tone-a" style="left:146px;top:297px"><div class="photo" role="img" aria-label="Portrait of a young girl smiling outdoors"></div></div>
  <div class="abs thumb tone-b" style="left:280px;top:297px"><div class="photo" role="img" aria-label="Two sisters hugging in the sun"></div></div>
  <div class="abs thumb tone-c" style="left:413px;top:297px"><div class="photo" role="img" aria-label="Girl with a flower in her hair"></div></div>
  <div class="abs thumb tone-d" style="left:543px;top:297px"><div class="photo" role="img" aria-label="Child sitting in tall dune grass"></div></div>
  <div class="abs thumb tone-a" style="left:673px;top:297px"><div class="photo" role="img" aria-label="Portrait of a young girl smiling outdoors"></div></div>
  <div class="abs thumb tone-b" style="left:807px;top:297px"><div class="photo" role="img" aria-label="Two sisters hugging in the sun"></div></div>
  <div class="abs thumb tone-c" style="left:940px;top:297px"><div class="photo" role="img" aria-label="Girl with a flower in her hair"></div></div>

  <div class="abs album-label" style="top:470px">ALBUM 2</div>
  <svg class="abs chev" style="left:113px;top:500px" viewBox="0 0 34 154"><polyline points="33,1 2,77 33,153" fill="none" stroke="#ccc" stroke-width="2"/></svg>
  <svg class="abs chev" style="left:1053px;top:500px" viewBox="0 0 34 154"><polyline points="1,1 32,77 1,153" fill="none" stroke="#ccc" stroke-width="2"/></svg>
  <div class="abs thumb tone-c" style="left:144px;top:521px"><div class="photo" role="img" aria-label="Girl with a flower in her hair"></div></div>
  <div class="abs thumb tone-b" style="left:277px;top:521px"><div class="photo" role="img" aria-label="Two sisters hugging in the sun"></div></div>
  <div class="abs thumb tone-a" style="left:411px;top:521px"><div class="photo" role="img" aria-label="Portrait of a young girl smiling outdoors"></div></div>
  <div class="abs thumb tone-d" style="left:540px;top:521px"><div class="photo" role="img" aria-label="Child sitting in tall dune grass"></div></div>
  <div class="abs thumb tone-c" style="left:671px;top:521px"><div class="photo" role="img" aria-label="Girl with a flower in her hair"></div></div>
  <div class="abs thumb tone-b" style="left:804px;top:521px"><div class="photo" role="img" aria-label="Two sisters hugging in the sun"></div></div>
  <div class="abs thumb tone-a" style="left:938px;top:521px"><div class="photo" role="img" aria-label="Portrait of a young girl smiling outdoors"></div></div>
</main>

<footer>
  <div class="abs footer-cap"></div>
  <div class="abs footer"></div>

  <section class="abs col" style="left:149px">
    <h3>SIMPLER THAN EVER</h3>
    <p>Lorem ipsum dolor sit amet, consectetur adipiscing elit. Nullam malesuada massa eget nisl rutrum ac hendrerit ante fermentum. Vestibulum ante ipsum primis in faucibus orci luctus et ultrices posuere cubilia Curae.</p>
    <a class="more" href="#">Learn More »</a>
  </section>
  <section class="abs col" style="left:381px">
    <h3>IMPRESSIVE PORTRAITS</h3>
    <p>Nullam malesuada massa eget nisl rutrum ac hendrerit ante fermentum. Vestibulum ante ipsum primis in faucibus orci luctus et ultrices posuere cubilia Curae. Lorem ipsum dolor sit amet, consectetur adipiscing.</p>
    <a class="more" href="#" style="margin-top:24px">See Portrait Gallery »</a>
  </section>
  <section class="abs col" style="left:614px">
    <h3>FROM THE BLOG</h3>
    <p>Lorem ipsum dolor sit amet, consectetur adipiscing elit.</p>
    <p>Nullam malesuada massa eget nisl rutrum ac hendrerit ante.</p>
    <p>Vestibulum ante ipsum primis in faucibus orci.</p>
    <a class="more" href="#">View All »</a>
  </section>
  <section class="abs col contact" style="left:848px">
    <h3>CONTACT US</h3>
    <p>Phone: +61 3 6200 418<br>Fax: +61 3 6200 419<br>Email: hi@maplelantern.example<br>L.N Some Streat Unknown<br>Location Of The Place<br>City - City Name<br>The Country</p>
    <a class="btn" href="#">Get In Touch</a>
  </section>

  <div class="abs base"></div>
  <div class="abs copyright">© Copyright - maple lantern photography</div>
  <div class="abs base-brand">
    <span class="base-brand-name">maple lantern</span>
    <span class="base-brand-sub">Photography</span>
  </div>
  <span class="abs social" style="left:936px" aria-label="Social profile"></span>
  <span class="abs social" style="left:972px" aria-label="Social profile"></span>
  <svg class="abs social" style="left:1009px" viewBox="0 0 27 27" aria-label="Email">
    <circle cx="13.5" cy="13.5" r="13.5" fill="#8a8a8a"/>
    <rect x="7" y="9" width="13" height="9" fill="#3a3a3a"/>
    <polyline points="7,9 13.5,14.5 20,9" fill="none" stroke="#8a8a8a" stroke-width="1.3"/>
  </svg>
</footer>

</body>
</html>
```